Building and Maintenance Company requires a flyer design, Specialising in domestic and commercial bu

We need a flyer design for a company based in Melbourne Victoria, we want to send the flyer out to businesses to obtain more work.

KEL Building and Construction provides the solution for all your building and maintenance needs

We have a professional and highly regarded team of reliable and skilled tradesmen who specialise in building services, domestic and commercial maintenance and gardening in Victoria and Tasmania.

Include our contact details;
0407 318 624
info@kelbuilding.com.au
www.kelbuilding.com.au

Target Market(s)

Domestic and Commercial Clients looking for building maintenance, window cleaning or gardening

Industry/Entity Type

It Company

Font styles to use
Sans Serif

Colors
33b8a4
474747
ffffff

Requirements
Must have
• Images and colour
Nice to have
• We would like the flyer to have our contact details on it.
• Colourful
• Clearly explains what we do, which is, 'KEL Building and Construction provides the solution for all your building, maintenance and gardening needs.'

```html
<!DOCTYPE html>
<html lang="en">
<head>
<meta charset="utf-8">
<title>KEL Building and Construction – Flyer</title>
<link href="https://fonts.googleapis.com/css2?family=Exo+2:wght@700&family=Oswald:wght@500&family=Raleway:wght@400&family=Lato:ital@1&family=Saira:wght@400&display=swap" rel="stylesheet">
<style>
  :root {
    --teal: #33b8a4;
    --teal-bright: #2fc4c0;
    --charcoal: #474747;
    --charcoal-deep: #2f2f2f;
    --light: #e9e9e9;
    --white: #ffffff;
    --ink: #2b2b2b;
  }
  * { margin: 0; padding: 0; box-sizing: border-box; }
  html, body { width: 855px; height: 1200px; overflow: hidden; background: var(--white); }
  .flyer { position: relative; width: 855px; height: 1200px; overflow: hidden; font-family: "Raleway", sans-serif; }
  .backdrop { position: absolute; inset: 0; }

  .brand { position: absolute; left: 40px; top: 52px; color: var(--white); font-family: "Exo 2", sans-serif; font-weight: 700; }
  .brand-mark { display: block; font-size: 176px; line-height: 1; letter-spacing: 4px; }
  .brand-line { display: block; font-size: 39px; line-height: 1.05; letter-spacing: 4px; text-transform: uppercase; margin-top: 6px; }

  .services-tag {
    position: absolute; left: 37px; top: 316px; width: 303px; height: 81px;
    border: 2px solid var(--teal); border-radius: 14px;
    color: var(--white); font-size: 23.5px; line-height: 1.2;
    display: flex; align-items: center; padding-left: 13px;
  }
  .call-line { position: absolute; left: 42px; top: 422px; font-size: 31px; color: var(--white); letter-spacing: -0.5px; }
  .call-line .number { color: var(--teal-bright); }

  .photo-circle {
    position: absolute; border-radius: 50%; background: var(--white);
    padding: 9px; box-shadow: 0 6px 16px rgba(0,0,0,.25);
  }
  .photo-circle .fill { width: 100%; height: 100%; border-radius: 50%; border: 4px solid var(--teal-bright); }
  .circle-window { left: 58px; top: 498px; width: 200px; height: 200px; }
  .circle-window .fill { background: linear-gradient(135deg, #bcdff2, #8fc6e8 55%, #e6e6e6); }
  .circle-plans { left: 324px; top: 455px; width: 208px; height: 208px; }
  .circle-plans .fill { background: linear-gradient(135deg, #f4f4f4, #d9d9d9 55%, #f2c200); }
  .circle-house { left: 606px; top: 410px; width: 208px; height: 208px; }
  .circle-house .fill { background: linear-gradient(135deg, #ffffff, #e4e4e4 60%, #b9a48a); }

  .intro {
    position: absolute; left: 41px; top: 742px; width: 487px;
    font-family: "Lato", sans-serif; font-style: italic; font-size: 16.5px; line-height: 21.5px;
    color: var(--ink); text-align: justify;
  }

  .garden-photo {
    position: absolute; left: 39px; top: 866px; width: 486px; height: 199px;
    border: 5px solid var(--teal-bright); box-shadow: 0 4px 10px rgba(0,0,0,.2);
    background: linear-gradient(180deg, #5e8a3a 0%, #c1456a 30%, #3f6b2a 55%, #8b6a4a 80%, #b9a58c 100%);
  }
  .site-photo {
    position: absolute; left: 592px; top: 686px; width: 223px; height: 137px;
    border: 4px solid var(--white); box-shadow: 0 4px 10px rgba(0,0,0,.2);
    background: linear-gradient(180deg, #9fcbe8 0%, #d9e7ef 45%, #e6b900 65%, #c9a27a 100%);
  }

  .contact-box {
    position: absolute; left: 566px; top: 864px; width: 289px; height: 108px;
    background: var(--charcoal-deep); border-top: 2px solid #dcdcdc; border-bottom: 2px solid #dcdcdc;
    padding: 10px 0 0 24px;
  }
  .contact-title { font-family: "Oswald", sans-serif; font-weight: 500; font-size: 33px; line-height: 1; color: var(--white); letter-spacing: 0.5px; }
  .contact-phone { font-size: 38px; line-height: 1.05; color: var(--teal-bright); }
  .contact-email { font-size: 18.5px; line-height: 1.1; color: var(--white); }

  .team-note {
    position: absolute; left: 583px; top: 1011px; width: 241px;
    font-family: "Saira", sans-serif; font-size: 12.3px; line-height: 14.6px;
    color: var(--white); text-align: justify; text-align-last: right;
  }

  .footer-line {
    position: absolute; left: 0; top: 1128px; width: 855px; height: 72px;
    display: flex; align-items: center; justify-content: center;
    font-family: "Saira", sans-serif; font-size: 20.5px; letter-spacing: 4.2px; color: var(--white);
  }
</style>
</head>
<body>
<div class="flyer">
  <svg class="backdrop" width="855" height="1200" viewBox="0 0 855 1200" aria-hidden="true">
    <defs>
      <linearGradient id="darkPanel" x1="0" y1="0" x2="1" y2="1">
        <stop offset="0" stop-color="#3d3d3d"/>
        <stop offset="0.6" stop-color="#555555"/>
        <stop offset="1" stop-color="#2c2c2c"/>
      </linearGradient>
      <linearGradient id="lightPanel" x1="0" y1="0" x2="1" y2="0">
        <stop offset="0" stop-color="#d6d6d6"/>
        <stop offset="0.5" stop-color="#f4f4f4"/>
        <stop offset="1" stop-color="#e1e1e1"/>
      </linearGradient>
      <linearGradient id="tealPanel" x1="0" y1="0" x2="0" y2="1">
        <stop offset="0" stop-color="#2ec6c0"/>
        <stop offset="1" stop-color="#39cbc4"/>
      </linearGradient>
      <linearGradient id="footerBand" x1="0" y1="0" x2="1" y2="0">
        <stop offset="0" stop-color="#3a3a3a"/>
        <stop offset="0.5" stop-color="#575757"/>
        <stop offset="1" stop-color="#3a3a3a"/>
      </linearGradient>
      <linearGradient id="workerScene" x1="0" y1="0" x2="0" y2="1">
        <stop offset="0" stop-color="#4f93cf"/>
        <stop offset="0.45" stop-color="#d6e3ec"/>
        <stop offset="0.7" stop-color="#8a8a8a"/>
        <stop offset="1" stop-color="#c9c3b8"/>
      </linearGradient>
    </defs>
    <rect width="855" height="1200" fill="url(#darkPanel)"/>
    <polygon points="565,490 855,440 855,1120 565,1120" fill="url(#tealPanel)"/>
    <polygon points="0,603 565,505 565,520 0,618" fill="var(--teal-bright)"/>
    <polygon points="0,618 565,520 565,1120 0,1120" fill="url(#lightPanel)"/>
    <rect x="0" y="1118" width="855" height="10" fill="var(--teal-bright)"/>
    <rect x="0" y="1128" width="855" height="72" fill="url(#footerBand)"/>
    <polygon points="384,0 855,0 855,470 640,472 384,394" fill="var(--teal-bright)"/>
    <polygon role="img" aria-label="Photo of a construction worker in a hard hat and hi-vis vest using a power tool on a building site"
             points="392,0 855,0 855,458 642,462 392,386" fill="url(#workerScene)"/>
  </svg>

  <div class="brand">
    <span class="brand-mark">KEL</span>
    <span class="brand-line">Building and<br>Construction</span>
  </div>

  <div class="services-tag">We are Offering Domestic<br>and Commercial Services</div>
  <p class="call-line">CALL <span class="number">0407 318 624</span></p>

  <div class="photo-circle circle-window"><div class="fill" role="img" aria-label="Photo of a woman cleaning a window with a cloth"></div></div>
  <div class="photo-circle circle-plans"><div class="fill" role="img" aria-label="Photo of building plans with a yellow hard hat and ruler"></div></div>
  <div class="photo-circle circle-house"><div class="fill" role="img" aria-label="Illustration of a house model under construction on blueprints"></div></div>

  <p class="intro">Specialising in domestic and commercial building maintenance, gardening and window cleaning. We provide accurate knowledge and maintain a professional relationship in order to achieve high quality results.</p>

  <div class="site-photo" role="img" aria-label="Photo of a builder in a hard hat working on a construction site"></div>
  <div class="garden-photo" role="img" aria-label="Photo of a landscaped garden with timber decking, steps and flowering plants"></div>

  <div class="contact-box">
    <p class="contact-title">CONTACT US TODAY</p>
    <p class="contact-phone">0407 318 624</p>
    <p class="contact-email">info@kelbuilding.com.au</p>
  </div>

  <p class="team-note">We have a professional and highly regarded team of reliable and skilled tradesmen who specialise in building services, domestic and commercial maintenance and gardening in Victoria and Tasmania.</p>

  <p class="footer-line">Please visit us to know more at - www.kelbuilding.com.au</p>
</div>
</body>
</html>
```